Brightmere Business Card Redesign & Logo Update

We need to update our business cards to something more modern and fresh. Brightmere can provide the current color schemes and old design examples, but welcome creativity in helping us with this redesign. PLEASE NOTE that we no longer utilize the "tree" and/or "leaf" imagery in our branding. If able would apprecaite an update on the quality of our "words only" logo in Ai. / PNG formats too.

Target Market(s)

Investors, landowners, corporate partners, contractors

Industry/Entity Type

Environmental Restoration & Conservation

Contact Information for Business Card

Logo, persons name, title, mailing address, phone and email, website url

Font styles to use
Other font styles liked:
• Merriweather

Requirements
Nice to have
• Logo, persons name, title, mailing address, phone and email, website url, but open to ideams
Should not have
• No all back backgrounds

```html
<!DOCTYPE html>
<html lang="en">
<head>
<meta charset="utf-8">
<title>Brightmere Business Card</title>
<link rel="stylesheet" href="https://fonts.googleapis.com/css2?family=Lato:wght@400;700;900&display=swap">
<style>
  :root {
    --bg: #b3b0b0;
    --charcoal: #3b3a3b;
    --orange: #ee7d0c;
    --green: #137a36;
    --white: #ffffff;
    --text-light: #f2f2f2;
  }
  html, body {
    margin: 0;
    padding: 0;
    width: 1200px;
    height: 1200px;
    overflow: hidden;
    background: var(--bg);
    font-family: "Lato", sans-serif;
  }
  .card {
    position: absolute;
    left: 281px;
    width: 642px;
    height: 366px;
    border-radius: 19px;
    overflow: hidden;
  }
  .card-front { top: 195px; background: var(--charcoal); }
  .card-back { top: 639px; background: var(--green); }
  .front-shape { position: absolute; inset: 0; }
  .person {
    position: absolute;
    left: 33px;
    top: 66px;
    color: var(--text-light);
  }
  .person-name {
    margin: 0;
    font-weight: 700;
    font-size: 27px;
    line-height: 1;
    color: var(--orange);
    letter-spacing: 0.2px;
  }
  .person-title {
    margin: 5px 0 0;
    font-size: 18px;
    font-weight: 400;
  }
  .contact-list {
    list-style: none;
    margin: 0;
    padding: 0;
    position: absolute;
    left: 34px;
    top: 135px;
    color: var(--text-light);
    font-size: 15.5px;
  }
  .contact-item {
    display: flex;
    align-items: flex-start;
    line-height: 22.4px;
  }
  .contact-item.address { margin-bottom: 7px; }
  .contact-icon {
    width: 13px;
    height: 13px;
    margin: 5px 10px 0 0;
    flex: none;
    fill: var(--orange);
  }
  .brand-front {
    position: absolute;
    left: 466px;
    top: 181px;
    transform: translate(-50%, -50%);
    margin: 0;
    font-weight: 900;
    font-size: 36px;
    line-height: 1;
    letter-spacing: 0.5px;
    color: var(--green);
    white-space: nowrap;
  }
  .card-back-texture {
    position: absolute;
    inset: 0;
    background: var(--green);
  }
  .brand-back {
    position: absolute;
    left: 50%;
    top: 50%;
    transform: translate(-50%, -50%);
    margin: 0;
    font-weight: 900;
    font-size: 64px;
    line-height: 1;
    letter-spacing: 2px;
    color: var(--white);
    white-space: nowrap;
  }
</style>
</head>
<body>

<section class="card card-front">
  <svg class="front-shape" width="642" height="366" viewBox="0 0 642 366" aria-hidden="true">
    <ellipse cx="625" cy="175" rx="357" ry="235" fill="var(--orange)"/>
    <ellipse cx="632" cy="180" rx="347" ry="228" fill="var(--white)"/>
    <ellipse cx="636" cy="184" rx="345" ry="226" fill="var(--green)"/>
    <ellipse cx="647" cy="180" rx="350" ry="222" fill="var(--white)"/>
  </svg>

  <div class="person">
    <h1 class="person-name">DANIEL HART</h1>
    <p class="person-title">Founder &amp; CEO</p>
  </div>

  <ul class="contact-list">
    <li class="contact-item address">
      <svg class="contact-icon" viewBox="0 0 14 14"><path d="M7 0a5 5 0 0 0-5 5c0 3.6 5 9 5 9s5-5.4 5-9a5 5 0 0 0-5-5zm0 7a2 2 0 1 1 0-4 2 2 0 0 1 0 4z"/></svg>
      <span>48 Alder Lane<br>Fernbrook, State 20417</span>
    </li>
    <li class="contact-item">
      <svg class="contact-icon" viewBox="0 0 14 14"><path d="M3 1l2.5 3-1.5 1.5c.8 1.8 2.2 3.2 4 4L9.5 8l3 2.5-1.5 2.5C6 13 1 8 1 2.5z"/></svg>
      <span>(555) 310-2284</span>
    </li>
    <li class="contact-item">
      <svg class="contact-icon" viewBox="0 0 14 14"><path d="M4 0h6a1 1 0 0 1 1 1v12a1 1 0 0 1-1 1H4a1 1 0 0 1-1-1V1a1 1 0 0 1 1-1zm.5 1.5v9h5v-9zM7 11.5a.8.8 0 1 0 0 1.6.8.8 0 0 0 0-1.6z"/></svg>
      <span>(555) 310-2285</span>
    </li>
    <li class="contact-item">
      <svg class="contact-icon" viewBox="0 0 14 14"><path d="M3 1h8v3H3zM1 5h12v6h-2V9H3v2H1zM4 10h6v4H4z"/></svg>
      <span>(555) 310-2286</span>
    </li>
    <li class="contact-item">
      <svg class="contact-icon" viewBox="0 0 14 14"><path d="M1 3h12v8H1zm1 1l5 4 5-4z" fill-rule="evenodd"/></svg>
      <span>hello@brightmere.com</span>
    </li>
    <li class="contact-item">
      <svg class="contact-icon" viewBox="0 0 14 14"><circle cx="7" cy="7" r="6.5"/><path d="M4 4c1 0 2 1 2 2s-1 1-1 2 1 2 0 3M9 2c0 1 1 2 2 2M10 8c-1 0-2 1-1 3" stroke="var(--charcoal)" stroke-width="1.2" fill="none"/></svg>
      <span>www.brightmere.com</span>
    </li>
  </ul>

  <h2 class="brand-front">BRIGHTMERE</h2>
</section>

<section class="card card-back">
  <div class="card-back-texture" role="img" aria-label="Subtle cracked-earth texture in deep green"></div>
  <h2 class="brand-back">BRIGHTMERE</h2>
</section>

</body>
</html>
```